Real Estate Text Messaging Info for house buyers and home sellers

We need a flyer (8 1/2 X 11) for a new service we are rolling out for my real estate business. It allows potential buyers to receive home information by texting "Lyle" to 48237. This will instantly send the potential buyer the price, information and photos of the home they are sitting in front of. This works for not only Lyle Ostrander's listings,but for ANY and ALL homes currently listed in the MLS.
Here is a link that will give you more information. http://www.zopply.example/index.aspx This is private labeled for Lyle Ostrander, Broker/Owner of Hallorin Realtors - Summit Estates and should not have Zopply anywhere in the flyer. I want the focus to be on receiving information instantly for buyers and for sellers it is an innovative way to promote their home. These should be two different types of flyers. I am looking for something that will grab potential buyers with the colors and the ease of use. Please include my website www.PineShoreHouseFacts.example and my phone number 555-274-CASA (2272).
Target Market(s)
home buyers and future home sellers
Industry/Entity Type
Real Estate
Look and feel
Each slider illustrates characteristics of the customer's brand and the style your logo design should communicate.

```html
<!DOCTYPE html>
<html lang="en">
<head>
<meta charset="utf-8">
<title>Text LYLE to 48237 – Home Info Flyer</title>
<link rel="stylesheet" href="https://fonts.googleapis.com/css2?family=Fira+Sans:wght@600;700&family=Kaushan+Script&display=swap">
<style>
  :root {
    --yellow: #f9dc06;
    --yellow-deep: #f2c200;
    --ink: #2a2206;
    --band: #231f20;
    --white: #ffffff;
    --red: #e8141b;
    --house-sky: #3b4a66;
    --house-glow: #c98a4a;
    --photo-warm: #c9956f;
    --photo-dark: #3a3230;
  }
  * { margin: 0; padding: 0; box-sizing: border-box; }
  html, body { width: 927px; height: 1200px; overflow: hidden; background: var(--yellow); }
  .flyer {
    position: relative; width: 927px; height: 1200px; overflow: hidden;
    background: radial-gradient(ellipse at 50% 55%, var(--yellow) 45%, var(--yellow-deep) 100%);
    font-family: "Fira Sans", "Helvetica Neue", Arial, sans-serif;
    color: var(--ink);
  }
  .house-photo {
    position: absolute; left: 360px; top: 0; width: 567px; height: 405px;
    background: linear-gradient(180deg, var(--house-sky) 0%, #5b5560 45%, var(--house-glow) 70%, #2f3a22 100%);
  }
  .phone-photo {
    position: absolute; left: 0; top: 0; width: 415px; height: 590px;
    background: linear-gradient(180deg, var(--photo-dark) 0%, var(--photo-warm) 100%);
  }
  .phone-screen {
    position: absolute; left: 118px; top: 90px; width: 224px; height: 328px;
    background: var(--white); text-align: center; overflow: hidden;
  }
  .phone-screen .cue {
    margin-top: 12px; font-weight: 700; font-size: 27px; line-height: 1.3; color: #111;
  }
  .red { color: var(--red); }
  .agent-portrait {
    position: absolute; left: 52px; bottom: 0; width: 170px; height: 200px;
    background: linear-gradient(180deg, #d9d9d9, #f4f4f4);
  }
  .lead {
    position: absolute; left: 415px; top: 430px; width: 512px;
    font-weight: 600; font-size: 48px; line-height: 58px; white-space: nowrap;
  }
  .band {
    position: absolute; left: 0; top: 591px; width: 927px; height: 246px;
    background: var(--band); text-align: center; color: var(--white);
  }
  .band .cta {
    margin-top: 18px; font-weight: 600; font-size: 70px; letter-spacing: 3px; line-height: 84px;
    white-space: nowrap;
  }
  .band .tagline {
    font-family: "Kaushan Script", cursive; font-size: 74px; line-height: 110px; margin-top: 2px;
    white-space: nowrap;
  }
  .promise {
    position: absolute; left: 0; top: 868px; width: 927px; text-align: center;
    font-weight: 700; font-size: 48px; line-height: 66px; white-space: nowrap;
  }
  .footer-brand {
    position: absolute; left: 20px; top: 1128px; width: 108px;
    font-weight: 700; font-size: 17px; line-height: 20px; color: var(--ink);
  }
  .footer-contact {
    position: absolute; left: 128px; top: 1126px; width: 790px; text-align: center;
    font-weight: 700; font-size: 20px; line-height: 29px; white-space: nowrap;
  }
</style>
</head>
<body>
  <main class="flyer">
    <div class="house-photo" role="img" aria-label="Modern glass-walled house lit warmly at dusk"></div>

    <div class="phone-photo" role="img" aria-label="Photo of a hand holding a smartphone"></div>
    <div class="phone-screen">
      <p class="cue">TEXT <span class="red">“LYLE”</span><br>TO <span class="red">48237</span></p>
      <div class="agent-portrait" role="img" aria-label="Portrait of the broker in shirt and tie"></div>
    </div>

    <p class="lead">For info on this home<br>or any home for sale</p>

    <section class="band">
      <p class="cta">TEXT <span class="red">“LYLE”</span> TO <span class="red">48237</span></p>
      <p class="tagline">Easy. Fast. Professional.</p>
    </section>

    <p class="promise">You will instantly receive the price,<br>information and photos of the home<br>you are sitting in front of.</p>

    <div class="footer-brand">Hallorin Realtors</div>
    <p class="footer-contact">Lyle Ostrander - Broker/Owner &nbsp;~&nbsp; Hallorin Realtors - Summit Estates<br>555-274-CASA (2272) &nbsp;~&nbsp; www.PineShoreHouseFacts.example</p>
  </main>
</body>
</html>
```